Design a flyer

Hi, I need a flyer designed for an electrical and air conditioning company based in brisbane, Australia.
We service the domestic market.
Flyer is to be double sided
Flyer size DL 210mm X 99mm
Was thinking one side services and discount coupons and the other side possible testimonials.
I have logo uploaded followed with the vehicle advertising, advertising stand alone sign and also business cards.
--------------------------
Coupon Cut out
save $150 OFF switchboard upgrades
save $150 Complimentary Electrical safety inspection
save $50 OFF Air Conditioner install or Service
save $50 next job if you leave feedback for first job
OVER $400 WORTH OF SAVINGS!
Our promise to you
* we will Arrive on time or we will pay you $100
* Before any job begins you will know the exact price
* We will leave your place as clean as we arrived
* if there is a problem and its our fault we will fix it for free
* provide a 12 month warranty on all parts
* we will provide friendly helpful service and advice
Phone number is 0487 625 903
Company Name - Tavolinex
License: 58164
ABN - 61 208 395 172
Also add vornel pay, zund and paklin logo at the bottom
----------------------------
Here is what some of my customers have had to say
Extremely professional...
“Arrived when he said he would, sent through a written quote and was very reasonable. He also checked out our smoke
detectors whist he was here. He installed 2 ceiling fans and an air conditioner. He
cleaned up the mess and was very efficient. I will definitely use him again and recommend
him to family and friends”
R.M – Stretton
“Excellent service provider. He arrived on time with a call before arriving, than carried all jobs quickly and efficiently and left no mess at all. I will definitely recommend his service to others requiring an electrician. Thanks again!”
K.S – Greenslopes
“Over the long weekend, I had problems with my power, not only did you pick up the first phone call but you came out at 5am to fix it. Love the fact you’re a 24hr service!”
T.W – Mount Gravatt
---------------------------
NEW changes
Hi everyone,
Just want to say well done all the designers look great!
I will soon be choosing a winner, but there are a couple of changes i would like to make, if you revise you will be in for a win.
Instead of Save 50 if you leave feedback for the first job quote. I want to change that put $110 cross out and put $71.50 Install & Supply LED Downlights (min 20)
I want this to be the number one followed by switch board upgrade cut out.
Also $50 off air con install - don't put service.
And the third testimonial T.W Make sure it has a full stop
Also keep in mind. It is an electrical & air conditioning company.
Be creative with your design, don't want to see any pictures of people as they are not working for us at this time.
Remember key focus, on coupons, phone numbers, and website. zund and vornelpay can be small and out of the way same with the license numbers.
Thank you
Good Luck!
Target Market(s)
Domestic Market - Home owners
Industry/Entity Type
Air Conditioning

```html
<!DOCTYPE html>
<html lang="en">
<head>
<meta charset="utf-8">
<title>Tavolinex DL Flyer</title>
<link rel="stylesheet" href="https://fonts.googleapis.com/css2?family=Open+Sans:wght@400;600;700;800&family=Oswald:wght@600&family=Yellowtail&display=swap">
<style>
:root{
  --blue:#1f6fc0;
  --blue-light:#3a93dc;
  --orange:#e8661c;
  --ink:#111;
  --paper:#fbfbfb;
  --stage:#e9e6e2;
  --white:#fff;
}
*{margin:0;padding:0;box-sizing:border-box}
html,body{width:1200px;height:1199px;overflow:hidden;background:var(--stage);font-family:"Open Sans",Arial,sans-serif;color:var(--ink)}
.flyer{position:absolute;width:452px;height:956px;background:var(--paper);overflow:hidden;box-shadow:0 4px 14px rgba(0,0,0,.25)}
.flyer--front{left:122px;top:74px}
.flyer--back{left:600px;top:190px}
.wave{position:absolute;left:0;width:100%}
.wave--top{top:0;height:120px}
.brand{position:absolute;left:0;width:100%;text-align:center;font-weight:400;font-size:44px;letter-spacing:3px;color:var(--blue)}
.brand::after{content:"";display:inline-block;width:12px;height:12px;margin-left:10px;background:var(--orange);border-radius:50%;vertical-align:middle}
.headline{position:absolute;top:188px;left:0;width:100%;text-align:center;font-weight:800;font-size:44px;line-height:45px}
.sectors{position:absolute;top:334px;left:0;width:100%;text-align:center;font-size:23px;line-height:29px;font-weight:600}
.dot{color:var(--orange);font-size:18px;margin:0 6px;vertical-align:2px}
.promise-title{position:absolute;top:428px;left:13px;color:var(--orange);font-weight:700;font-size:23px}
.promise-list{position:absolute;top:466px;left:20px;width:415px;list-style:none;font-size:12.8px;font-weight:600;line-height:17.5px}
.promise-list li{position:relative;padding-left:18px;margin-bottom:5px}
.promise-list li::before{content:"";position:absolute;left:0;top:5px;width:8px;height:8px;border-radius:50%;background:var(--orange)}
.savings-panel{position:absolute;left:0;top:585px;width:100%;height:371px}
.savings-title{position:absolute;top:642px;left:0;width:100%;text-align:center;color:var(--white);font-weight:700;font-size:22px}
.coupons{position:absolute;top:686px;left:20px;width:412px;height:182px;display:grid;grid-template-columns:1fr 1fr;grid-template-rows:1fr 1fr;border:2px dashed var(--white)}
.coupon{position:relative;color:var(--white);text-align:center;border:0 dashed var(--white)}
.coupon:nth-child(1){border-right-width:2px;border-bottom-width:2px}
.coupon:nth-child(2){border-bottom-width:2px}
.coupon:nth-child(3){border-right-width:2px}
.offer{display:flex;align-items:center;justify-content:center;gap:6px;margin-top:10px;height:38px}
.save{font-family:"Yellowtail",cursive;color:var(--orange);font-size:26px;line-height:1;transform:rotate(-12deg);margin-top:-8px}
.amount{font-family:"Oswald",sans-serif;font-weight:600;font-size:30px;line-height:36px}
.detail{display:block;font-size:13.5px;line-height:15px}
.contact{position:absolute;left:15px;color:var(--white)}
.contact-label{font-size:15px}
.phone{font-weight:700;font-size:20px;display:flex;align-items:center;gap:8px;margin-top:2px}
.phone svg{width:20px;height:16px}
.web{font-size:14px;margin-top:1px}
.payments{position:absolute;right:14px;display:flex;gap:3px}
.pay{width:58px;height:34px;background:var(--white);border-radius:3px;display:flex;align-items:center;justify-content:center;font-size:10px;font-weight:700;color:var(--blue);white-space:nowrap}
.legal{position:absolute;right:14px;color:var(--white);font-size:10px}
.flyer--front .contact{top:885px}
.flyer--front .payments{top:888px}
.flyer--front .legal{top:930px}
.flyer--back .contact{top:879px}
.flyer--back .payments{top:890px}
.flyer--back .legal{top:934px}
.reviews-title{position:absolute;top:230px;left:21px;width:410px;font-weight:700;font-size:21px;line-height:26px}
.review{position:absolute;left:18px;width:420px;font-size:15px;line-height:20px}
.review-author{display:block;margin-top:6px;color:var(--orange);font-weight:700;font-size:15px}
.contact-panel{position:absolute;left:0;top:830px;width:100%;height:126px}
</style>
</head>
<body>

<section class="flyer flyer--front">
  <svg class="wave wave--top" viewBox="0 0 452 120" preserveAspectRatio="none" aria-hidden="true">
    <path d="M0 0H452V55C380 10 250 5 160 30 90 48 40 70 0 90Z" fill="var(--blue)"/>
    <path d="M0 45C60 22 150 8 240 20 300 28 330 50 320 75 290 50 220 38 140 50 80 60 30 80 0 95Z" fill="var(--orange)"/>
  </svg>
  <div class="brand" style="top:100px">Tavolinex</div>

  <h1 class="headline">ELECTRICAL &amp;<br>AIR CONIDTIONAL<br>SERVICES</h1>
  <p class="sectors">Domestic <span class="dot">●</span> Commercial <span class="dot">●</span> Intall<br>Service <span class="dot">●</span> Maintenance</p>

  <h2 class="promise-title">OUR PROMISE TO YOU</h2>
  <ul class="promise-list">
    <li>We will Arrive on time or we will pay you $100</li>
    <li>Before any job begins you will know the exact price We will leave your place as clean as we arrived</li>
    <li>If there is a problem and its our fault we will fix it for free</li>
    <li>Provide a 12 month warranty on all parts</li>
    <li>We will provide friendly helpful service and advice</li>
  </ul>

  <svg class="savings-panel" viewBox="0 0 452 371" preserveAspectRatio="none" aria-hidden="true">
    <defs>
      <linearGradient id="panelFront" x1="0" y1="0" x2="0" y2="1">
        <stop offset="0" stop-color="var(--blue-light)"/>
        <stop offset="1" stop-color="var(--blue)"/>
      </linearGradient>
    </defs>
    <path d="M0 20C120 40 300 30 452 0V371H0Z" fill="var(--orange)"/>
    <path d="M0 32C140 50 320 38 452 14V371H0Z" fill="url(#panelFront)"/>
  </svg>
  <h2 class="savings-title">OVER $400 WORTH OF SAVINGS</h2>
  <div class="coupons">
    <div class="coupon"><div class="offer"><span class="save">Save</span><span class="amount">$150 OFF</span></div><span class="detail">switchboard upgrades<br>2nd line</span></div>
    <div class="coupon"><div class="offer"><span class="save">Save</span><span class="amount">$150</span></div><span class="detail">Complimentary Electrical<br>Safety Inspection</span></div>
    <div class="coupon"><div class="offer"><span class="save">Save</span><span class="amount">$50 OFF</span></div><span class="detail">Air Conditioner install<br>or Services</span></div>
    <div class="coupon"><div class="offer"><span class="save">Save</span><span class="amount">$50</span></div><span class="detail">Next job if you leave<br>feedback for first job</span></div>
  </div>

  <div class="contact">
    <p class="contact-label">Contact Us:</p>
    <p class="phone"><svg viewBox="0 0 20 16" aria-hidden="true"><path d="M1 5C1 2 5 1 10 1S19 2 19 5V7H14V5H6V7H1Z M4 8H16L18 15H2Z" fill="currentColor"/></svg>0487 625 903</p>
    <p class="web">www.Tavolinex.com.au</p>
  </div>
  <div class="payments"><span class="pay">zund</span><span class="pay">vornelpay</span><span class="pay">paklin</span></div>
  <p class="legal">License: 58164 &nbsp; ABN: 61 208 395 172</p>
</section>

<section class="flyer flyer--back">
  <svg class="wave wave--top" viewBox="0 0 452 120" preserveAspectRatio="none" aria-hidden="true">
    <path d="M0 0H452V90C400 55 300 30 200 25 120 22 50 40 0 60Z" fill="var(--blue)"/>
    <path d="M0 40C80 20 180 15 260 30 320 42 340 60 330 80 290 58 210 45 130 52 70 58 30 75 0 95Z" fill="var(--orange)"/>
  </svg>
  <div class="brand" style="top:110px">Tavolinex</div>

  <h2 class="reviews-title">Here is what some of my customers have had to say</h2>

  <blockquote class="review" style="top:300px">“Extremely professional...<br>Arrived when he said he would, sent through a written quote and was very reasonable. He also checked out our smoke detectors whist he was here. He installed 2 ceiling fans and an air conditioner. He cleaned up the mess and was very efficient. I will definitely use him again and recommend him to family and friends”<span class="review-author">R.M – Stretton</span></blockquote>

  <blockquote class="review" style="top:512px">“Excellent service provider. He arrived on time with a call before arriving, than carried all jobs quickly and efficiently and left no mess at all. I will definitely recommend his service to others requiring an electrician. Thanks again!”<span class="review-author">K.S – Greenslopes</span></blockquote>

  <blockquote class="review" style="top:676px">“Over the long weekend, I had problems with my power, not only did you pick up the first phone call but you came out at 5am to fix it. Love the fact you’re a 24hr service!”<span class="review-author">T.W – Mount Gravatt</span></blockquote>

  <svg class="contact-panel" viewBox="0 0 452 126" preserveAspectRatio="none" aria-hidden="true">
    <defs>
      <linearGradient id="panelBack" x1="0" y1="0" x2="0" y2="1">
        <stop offset="0" stop-color="var(--blue-light)"/>
        <stop offset="1" stop-color="var(--blue)"/>
      </linearGradient>
    </defs>
    <path d="M0 12C150 20 320 22 452 0V126H0Z" fill="var(--orange)"/>
    <path d="M0 20C150 32 320 34 452 12V126H0Z" fill="url(#panelBack)"/>
  </svg>
  <div class="contact">
    <p class="contact-label">Contact Us:</p>
    <p class="phone"><svg viewBox="0 0 20 16" aria-hidden="true"><path d="M1 5C1 2 5 1 10 1S19 2 19 5V7H14V5H6V7H1Z M4 8H16L18 15H2Z" fill="currentColor"/></svg>0487 625 903</p>
    <p class="web">www.Tavolinex.com.au</p>
  </div>
  <div class="payments"><span class="pay">zund</span><span class="pay">vornelpay</span><span class="pay">paklin</span></div>
  <p class="legal">License: 58164 &nbsp; ABN: 61 208 395 172</p>
</section>

</body>
</html>
```